Business Card Design Wenda Style

I make Hand Made Name necklaces which are known as Wenda Style and would like a Shiny Gold Business Card almost to look like a Gold Bar.
on the 2nd side I want an image of a Wenda Necklace in Silver as it will be on a Gold Background.

Industry/Entity Type

Business

Contact Information for Business Card

Dunvok Jewellery UK
Loop Pendants 2 Go

Hugo Penwright
Director
M: 07700 914 263

www.dunvokjwl.co.uk

Requirements
Must have
• Writing must be in Black

Card must be metallic gold

```html
<!DOCTYPE html>
<html lang="en">
<head>
<meta charset="utf-8">
<title>Hugo Penwright – Business Card</title>
<link rel="stylesheet" href="https://fonts.googleapis.com/css2?family=Antonio:wght@400;600&display=swap">
<style>
  :root {
    --gold-deep: #ad8700;
    --gold-mid: #d2c21a;
    --gold-bright: #e8f230;
    --gold-soft: rgba(190, 160, 10, 0.35);
    --ink: #000000;
    --card-w: 1200px;
    --card-h: 791px;
  }
  html, body {
    margin: 0;
    padding: 0;
    width: var(--card-w);
    height: var(--card-h);
    overflow: hidden;
    background: var(--gold-deep);
  }
  .card {
    position: relative;
    width: var(--card-w);
    height: var(--card-h);
    overflow: hidden;
    background:
      linear-gradient(90deg,
        var(--gold-deep) 0%,
        var(--gold-mid) 28%,
        var(--gold-bright) 52%,
        var(--gold-bright) 58%,
        var(--gold-mid) 80%,
        var(--gold-deep) 100%);
    font-family: "Antonio", "Arial Narrow", sans-serif;
    color: var(--ink);
  }
  .card__shine {
    position: absolute;
    inset: 0;
    background: linear-gradient(180deg, rgba(255,255,255,0.08) 0%, rgba(255,255,255,0) 45%, rgba(0,0,0,0.06) 100%);
  }
  .ornament-cluster {
    position: absolute;
    left: 915px;
    top: 60px;
    width: 275px;
    height: 325px;
    border-radius: 40%;
    background: radial-gradient(ellipse at 35% 55%, var(--gold-soft) 0%, rgba(190,160,10,0) 70%);
  }
  .ornament-band {
    position: absolute;
    left: 70px;
    top: 558px;
    width: 1050px;
    height: 22px;
    border-radius: 11px;
    background: linear-gradient(180deg, rgba(190,160,10,0) 0%, var(--gold-soft) 50%, rgba(190,160,10,0) 100%);
  }
  .identity {
    position: absolute;
    left: 0;
    width: 100%;
    text-align: center;
    font-variant: small-caps;
    margin: 0;
  }
  .identity__name {
    top: 244px;
    left: 4px;
    font-size: 78px;
    font-weight: 600;
    line-height: 1;
    letter-spacing: 2px;
  }
  .identity__role {
    top: 348px;
    left: -20px;
    font-size: 50px;
    font-weight: 400;
    line-height: 1;
    letter-spacing: 2px;
  }
  .contact {
    position: absolute;
    left: 69px;
    top: 594px;
    margin: 0;
    line-height: 1;
    text-transform: uppercase;
  }
  .contact__phone {
    display: block;
    font-size: 40px;
    letter-spacing: 0;
  }
  .contact__web {
    display: block;
    margin-top: 4px;
    font-size: 31px;
    letter-spacing: 0;
  }
</style>
</head>
<body>
<main class="card">
  <div class="card__shine"></div>

  <div class="ornament-cluster" role="img" aria-label="Decorative cluster of glowing gold beads"></div>
  <div class="ornament-band" role="img" aria-label="Decorative row of small gold beads"></div>

  <h1 class="identity identity__name">Hugo Penwright</h1>
  <p class="identity identity__role">Director</p>

  <p class="contact">
    <span class="contact__phone">M: 07700 914 263</span>
    <span class="contact__web">www.dunvokjwl.co.uk</span>
  </p>
</main>
</body>
</html>
```